Business Card Design Project

Doctor, Pain Management. Need a new business card design with appointment info on the back. New address is 18 Birchwood Court, Suite 304, Holloway, NJ 07519. Right now I believe the rest of the information is staying the same.

```html
<!DOCTYPE html>
<html lang="en">
<head>
<meta charset="utf-8">
<title>Kindred Pain Care – Business Card</title>
<link rel="stylesheet" href="https://fonts.googleapis.com/css2?family=Federo&family=Crimson+Text:ital,wght@0,400;0,700;1,400;1,700&display=swap">
<style>
  :root {
    --backdrop: #d6ecf8;
    --card-black: #000000;
    --brand-blue: #0089c0;
    --brand-yellow: #f6ec1b;
    --cream: #fffbd2;
    --white: #ffffff;
    --ink: #111111;
    --display: "Federo", sans-serif;
    --serif: "Crimson Text", serif;
  }
  html, body {
    margin: 0;
    width: 1200px;
    height: 1200px;
    overflow: hidden;
    background: var(--backdrop);
  }
  .card {
    position: absolute;
    left: 144px;
    width: 912px;
    display: block;
  }
  .card-front { top: 29px; height: 547px; }
  .card-back { top: 624px; height: 546px; }
  .display { font-family: var(--display); }
  .serif { font-family: var(--serif); }
  .italic { font-style: italic; }
  .bold { font-weight: 700; }
</style>
</head>
<body>

<!-- Front of card -->
<svg class="card card-front" viewBox="0 0 912 547" xmlns="http://www.w3.org/2000/svg" aria-label="Business card front">
  <rect class="front-top" x="0" y="0" width="912" height="365" fill="var(--card-black)"/>
  <rect class="contact-band" x="0" y="365" width="912" height="182" fill="var(--brand-blue)"/>

  <!-- name plate -->
  <path class="plate-accent" d="M 372 365 C 338 318, 340 240, 466 216 C 600 190, 800 180, 912 180 L 912 186 C 800 186, 600 195, 470 225 C 360 250, 360 320, 392 365 Z" fill="var(--brand-yellow)"/>
  <path class="name-plate" d="M 392 365 C 360 320, 360 250, 470 225 C 600 195, 800 186, 912 186 L 912 365 Z" fill="var(--white)"/>

  <!-- brand mark stand-in -->
  <g class="brand-mark">
    <circle cx="88" cy="128" r="26" fill="var(--brand-blue)"/>
    <text class="display" x="124" y="122" font-size="24" fill="var(--white)">Kindred</text>
    <text class="display" x="124" y="150" font-size="24" fill="var(--white)">Pain Care</text>
  </g>

  <text class="display practice-name" x="256" y="122" font-size="58" textLength="592" lengthAdjust="spacingAndGlyphs" fill="var(--brand-yellow)">Kindred Pain Care</text>

  <!-- locations -->
  <g class="locations">
    <path d="M 70 303 a 10 10 0 0 1 10 10 c 0 8 -10 24 -10 24 c 0 0 -10 -16 -10 -24 a 10 10 0 0 1 10 -10 z" fill="var(--brand-yellow)"/>
    <circle cx="70" cy="313" r="4" fill="var(--card-black)"/>
    <text class="serif italic" x="90" y="313" font-size="21" fill="var(--white)">Locations in</text>
    <text class="serif italic" x="90" y="338" font-size="21" textLength="199" lengthAdjust="spacingAndGlyphs" fill="var(--white)">New Jersey &amp; New York</text>
  </g>

  <text class="display doctor-name" x="848" y="291" text-anchor="end" font-size="41" textLength="434" lengthAdjust="spacingAndGlyphs" fill="var(--ink)">Lena Hartwell, M.D., Ph.D.</text>
  <text class="serif italic doctor-title" x="848" y="336" text-anchor="end" font-size="32" textLength="368" lengthAdjust="spacingAndGlyphs" fill="var(--ink)">Board Certified Anesthiologist</text>

  <g class="address serif italic" font-size="25" fill="var(--white)">
    <text x="62" y="413">18 Birchwood Court, Suite 304</text>
    <text x="62" y="446">Holloway, NJ 07519</text>
    <text class="bold" x="62" y="479" textLength="167" lengthAdjust="spacingAndGlyphs">kindredpaincare.com</text>
  </g>
  <g class="contact serif italic" font-size="26" fill="var(--white)" text-anchor="end">
    <text x="854" y="413" textLength="176" lengthAdjust="spacingAndGlyphs">P: 555.204.3318</text>
    <text x="854" y="446" textLength="176" lengthAdjust="spacingAndGlyphs">F: 555.204.3390</text>
    <text class="bold" x="854" y="479" textLength="404" lengthAdjust="spacingAndGlyphs">frontdesk@kindredpaincare.com</text>
  </g>
</svg>

<!-- Back of card -->
<svg class="card card-back" viewBox="0 0 912 546" xmlns="http://www.w3.org/2000/svg" aria-label="Appointment card back">
  <rect x="0" y="0" width="912" height="546" fill="var(--card-black)"/>

  <path class="form-panel" d="M 0 148 Q 456 108 912 148 L 912 412 Q 456 452 0 412 Z" fill="var(--cream)" stroke="var(--white)" stroke-width="5"/>

  <text class="serif italic" x="62" y="100" font-size="28" textLength="176" lengthAdjust="spacingAndGlyphs" fill="var(--white)">P: 555.204.3318</text>
  <text class="display" x="454" y="98" text-anchor="middle" font-size="44" textLength="212" lengthAdjust="spacingAndGlyphs" fill="var(--brand-yellow)">Appointment</text>
  <text class="serif italic" x="850" y="100" text-anchor="end" font-size="28" textLength="176" lengthAdjust="spacingAndGlyphs" fill="var(--white)">F: 555.204.3390</text>

  <g class="form-fields serif" font-size="27" fill="var(--ink)">
    <text x="62" y="192">For:</text>
    <line x1="62" y1="200" x2="852" y2="200" stroke="var(--ink)" stroke-width="1.5"/>

    <g class="weekdays" font-size="28">
      <g transform="translate(66,0)"><rect x="0" y="240" width="15" height="15" fill="none" stroke="var(--ink)" stroke-width="2"/><path d="M 3 257 H 17 V 243" fill="none" stroke="var(--ink)" stroke-width="2"/><text x="24" y="259">Mon</text></g>
      <g transform="translate(193,0)"><rect x="0" y="240" width="15" height="15" fill="none" stroke="var(--ink)" stroke-width="2"/><path d="M 3 257 H 17 V 243" fill="none" stroke="var(--ink)" stroke-width="2"/><text x="24" y="259">Tue</text></g>
      <g transform="translate(309,0)"><rect x="0" y="240" width="15" height="15" fill="none" stroke="var(--ink)" stroke-width="2"/><path d="M 3 257 H 17 V 243" fill="none" stroke="var(--ink)" stroke-width="2"/><text x="24" y="259">Wed</text></g>
      <g transform="translate(435,0)"><rect x="0" y="240" width="15" height="15" fill="none" stroke="var(--ink)" stroke-width="2"/><path d="M 3 257 H 17 V 243" fill="none" stroke="var(--ink)" stroke-width="2"/><text x="24" y="259">Thu</text></g>
      <g transform="translate(556,0)"><rect x="0" y="240" width="15" height="15" fill="none" stroke="var(--ink)" stroke-width="2"/><path d="M 3 257 H 17 V 243" fill="none" stroke="var(--ink)" stroke-width="2"/><text x="24" y="259">Fri</text></g>
      <g transform="translate(659,0)"><rect x="0" y="240" width="15" height="15" fill="none" stroke="var(--ink)" stroke-width="2"/><path d="M 3 257 H 17 V 243" fill="none" stroke="var(--ink)" stroke-width="2"/><text x="24" y="259">Sat</text></g>
      <g transform="translate(768,0)"><rect x="0" y="240" width="15" height="15" fill="none" stroke="var(--ink)" stroke-width="2"/><path d="M 3 257 H 17 V 243" fill="none" stroke="var(--ink)" stroke-width="2"/><text x="24" y="259">Sun</text></g>
    </g>

    <text x="62" y="339">Date:</text>
    <text x="488" y="339">Time:</text>
    <line x1="62" y1="348" x2="852" y2="348" stroke="var(--ink)" stroke-width="1.5"/>

    <g class="italic" text-anchor="middle" font-size="27">
      <text x="456" y="380" textLength="474" lengthAdjust="spacingAndGlyphs">If you are unable to keep your appointment,</text>
      <text x="456" y="413" textLength="396" lengthAdjust="spacingAndGlyphs">please contact us as soon as possible.</text>
    </g>
  </g>

  <text class="serif italic bold" x="62" y="472" font-size="25" textLength="167" lengthAdjust="spacingAndGlyphs" fill="var(--brand-yellow)">kindredpaincare.com</text>
  <text class="serif italic bold" x="850" y="472" text-anchor="end" font-size="26" textLength="405" lengthAdjust="spacingAndGlyphs" fill="var(--brand-yellow)">frontdesk@kindredpaincare.com</text>
</svg>

</body>
</html>
```